Referal Program Sign

Need two graphics layouts for banners to get printed one 20x20 and another 26x26 about our referral program. WE LOVE REFERRALS " Do you have friends and family that could use our services? Refer them to us and when they open a new agreement, you pick an agreement on your account for a two-week credit!

```html
<!DOCTYPE html>
<html lang="en">
<head>
<meta charset="utf-8">
<title>Referral Program Signs</title>
<link rel="stylesheet" href="https://fonts.googleapis.com/css2?family=Barlow:ital,wght@0,500;0,600;0,700;1,500;1,600&family=Barlow+Condensed:wght@600;700&display=swap">
<style>
  :root {
    --backdrop: #e9eaec;
    --paper: #ffffff;
    --sky: #3fb3ec;
    --sky-deep: #2a8fd0;
    --navy: #24345a;
    --brand-blue: #1b62a8;
    --orange: #f08a2c;
    --purple: #7b3aa6;
    --purple-deep: #5e2890;
    --gold: #f7b52a;
    --ink: #1c1c1c;
  }
  * { box-sizing: border-box; margin: 0; padding: 0; }
  html, body { width: 1200px; height: 856px; overflow: hidden; background: var(--backdrop); }
  .canvas {
    width: 1200px; height: 856px;
    display: flex; justify-content: center; align-items: center; gap: 60px;
  }
  .sign {
    position: relative; background: var(--paper); overflow: hidden;
    box-shadow: 0 6px 18px rgba(0,0,0,.18);
  }
  .sign--sky { width: 480px; height: 480px; }
  .sign--violet { width: 540px; height: 540px; }

  .footer-band { position: absolute; inset: 0; width: 100%; height: 100%; }

  .banner-art {
    position: absolute; border-radius: 18px;
    display: flex; flex-direction: column; justify-content: center; align-items: center;
    font-family: "Barlow Condensed", sans-serif; font-weight: 700; line-height: 1;
  }
  .banner-line { display: block; }

  .headline {
    position: absolute;
    font-family: "Barlow", sans-serif; font-weight: 600; color: var(--brand-blue);
  }
  .offer {
    position: absolute;
    font-family: "Barlow", sans-serif; font-style: italic; font-weight: 600; color: var(--ink);
  }
  .offer-line { display: block; white-space: nowrap; }
  .brand {
    position: absolute; left: 0; right: 0;
    display: flex; justify-content: center; align-items: center; gap: 10px;
  }
  .brand-dot { width: 30px; height: 30px; border-radius: 50%; }
  .brand-name {
    font-family: "Barlow", sans-serif; font-weight: 600; font-size: 30px;
    color: var(--brand-blue); letter-spacing: .5px; line-height: 1;
  }

  /* 20x20 sign */
  .sign--sky .banner-art {
    left: 55px; top: 18px; width: 364px; height: 172px;
    background: linear-gradient(160deg, var(--sky) 0%, var(--sky-deep) 100%);
    color: #ffffff;
  }
  .sign--sky .banner-line--top { font-size: 44px; }
  .sign--sky .banner-line--main { font-size: 44px; margin-top: 6px; }
  .sign--sky .headline { left: 42px; right: 29px; top: 198px; font-size: 26px; line-height: 33px; }
  .sign--sky .offer { left: 42px; right: 29px; top: 276px; font-size: 20.5px; line-height: 29px; }
  .sign--sky .offer-line { white-space: normal; text-align: justify; text-align-last: justify; }
  .sign--sky .offer-line:last-child { text-align-last: left; }
  .sign--sky .brand { top: 376px; }
  .sign--sky .brand-dot { background: var(--orange); }

  /* 26x26 sign */
  .sign--violet .banner-art {
    left: 119px; top: 28px; width: 336px; height: 240px;
    background: linear-gradient(160deg, var(--purple) 0%, var(--purple-deep) 100%);
  }
  .sign--violet .banner-line--top { font-size: 46px; color: var(--gold); }
  .sign--violet .banner-line--main { font-size: 48px; color: #ffffff; margin-top: 8px; }
  .sign--violet .headline {
    left: 47px; right: 40px; top: 278px; font-size: 22.5px; line-height: 29px; text-transform: uppercase;
  }
  .sign--violet .offer { left: 47px; right: 40px; top: 340px; font-size: 20px; line-height: 29px; font-weight: 500; }
  .sign--violet .brand { top: 440px; }
  .sign--violet .brand-dot { background: var(--brand-blue); }
</style>
</head>
<body>
<main class="canvas">

  <section class="sign sign--sky" aria-label="Referral sign, orange edition">
    <svg class="footer-band" viewBox="0 0 480 480" aria-hidden="true">
      <path d="M0 436 Q240 486 480 400 L480 480 L0 480 Z" fill="var(--orange)"/>
    </svg>
    <div class="banner-art" role="img" aria-label="Speech bubble banner illustration with megaphone">
      <span class="banner-line banner-line--top">WE LOVE</span>
      <span class="banner-line banner-line--main">REFERRALS</span>
    </div>
    <h2 class="headline">Do you have friends and family<br>that could use our services?</h2>
    <p class="offer">
      <span class="offer-line">Refer them to us and when they open a</span>
      <span class="offer-line">new agreement, you pick an agreement</span>
      <span class="offer-line">on your account for a two-week credit!</span>
    </p>
    <div class="brand"><span class="brand-dot"></span><span class="brand-name">HARBOR HOME</span></div>
  </section>

  <section class="sign sign--violet" aria-label="Referral sign, blue edition">
    <svg class="footer-band" viewBox="0 0 540 540" aria-hidden="true">
      <path d="M0 490 Q250 530 540 462 L540 540 L0 540 Z" fill="var(--brand-blue)"/>
    </svg>
    <div class="banner-art" role="img" aria-label="Speech bubble banner illustration with megaphone">
      <span class="banner-line banner-line--top">WE LOVE</span>
      <span class="banner-line banner-line--main">REFERRALS</span>
    </div>
    <h2 class="headline">Do you have friends and family<br>that could use our services?</h2>
    <p class="offer">
      <span class="offer-line">Refer them to us and when they open a new</span>
      <span class="offer-line">agreement, you pick an agreement on your</span>
      <span class="offer-line">account for a two-week credit!</span>
    </p>
    <div class="brand"><span class="brand-dot"></span><span class="brand-name">HARBOR HOME</span></div>
  </section>

</main>
</body>
</html>
```